Mailchimp Template Design

We are looking to create two types of email template for use specifically within Mailchimp including a Newsletter Template Layout and a Campaign Template Layout, as such require the templates to be designed in HTML to be compatible with Mailchimp.

The Newsletter Template Layout should accommodate for three newsletter article features and two separate product offer features. Each newsletter article feature should contain: A small image (16:9 ratio), a Feature title and up to 100 words as a short description and each Product offer feature should show a large image (4:3 ratio) and short description of

The Campaign Template Layout should accommodate for one large (4:3 ratio) campaign image, a small description of 50 words and three product offer areas.

The look and feel of the designs should be consistent with the Brisk Lane website (www.brisklane.co.uk) and the uploaded source material that is attached to this project brief.
Updates

Reason: Review of other business marketing efforts to see which design is the most contextually relevant.

Target Market(s)

Pet Owning Consumer

Industry/Entity Type

Pet Shop

Number of Pages Required

2 page

Other font styles liked:
• Provided in Brief Attachment

Requirements
Must have
• Compatibility with Mail Chimp
• Consistency with Brisk Lane (www.brisklane.co.uk) Look & Feel and Brand Guidelines

```html
<!DOCTYPE html>
<html lang="en">
<head>
<meta charset="utf-8">
<title>Brisk Lane Newsletter</title>
<link href="https://fonts.googleapis.com/css2?family=Fredoka:wght@500;600&family=Roboto:wght@400;500;700&display=swap" rel="stylesheet">
<style>
  :root {
    --sky: #5bb9e7;
    --blue: #3aa8df;
    --title-blue: #2a9fd8;
    --amber: #fbbf55;
    --rule: #f5bd45;
    --ink: #3a3a3a;
    --white: #ffffff;
  }
  * { margin: 0; padding: 0; box-sizing: border-box; }
  html, body { width: 1200px; height: 3056px; overflow: hidden; background: var(--white); }
  body { position: relative; font-family: "Roboto", Arial, sans-serif; color: var(--ink); }

  .preheader {
    position: absolute; left: 0; top: 0; width: 1200px; height: 37px;
    background: var(--sky); color: var(--white); font-size: 12px;
  }
  .preheader .view { position: absolute; left: 275px; top: 11px; }
  .preheader .forward { position: absolute; left: 815px; top: 11px; }
  .preheader a { color: var(--white); }

  .masthead {
    position: absolute; left: 0; top: 37px; width: 1200px; height: 142px;
    background: var(--blue); display: flex; align-items: center; justify-content: center; gap: 14px;
  }
  .brand-name { font-family: "Fredoka", sans-serif; font-weight: 600; font-size: 56px; color: var(--white); letter-spacing: 1px; }
  .brand-dot { width: 22px; height: 22px; border-radius: 50%; background: var(--white); }

  .article { position: absolute; left: 275px; width: 652px; text-align: center; }
  .article .photo { width: 652px; height: 308px; }
  .article h2 {
    margin-top: 28px; font-size: 26px; font-weight: 500; color: var(--title-blue); line-height: 32px;
  }
  .article p { margin: 10px auto 0; width: 620px; font-size: 14.5px; line-height: 23px; }
  .button {
    display: block; width: 202px; height: 53px; margin: 22px auto 0; border-radius: 6px;
    background: var(--amber); color: var(--white); font-family: "Fredoka", sans-serif;
    font-weight: 500; font-size: 19px; line-height: 53px; text-align: center; text-decoration: none;
  }
  .rule { position: absolute; left: 230px; width: 730px; height: 3px; background: var(--rule); }

  .cockatiel { top: 228px; }
  .cockatiel .photo { background: linear-gradient(110deg, #5a5a60 0%, #c9c7a0 35%, #e4e7f3 60%, #f3f5fb 100%); }
  .frog { top: 894px; }
  .frog .photo { background: linear-gradient(100deg, #2b2b24 0%, #5c9d2b 40%, #7cc23a 60%, #2f4a1e 100%); }
  .horses { top: 1556px; }
  .horses .photo { background: linear-gradient(180deg, #7fa9c9 0%, #c9dbe8 45%, #7a5a42 70%, #4f7a2e 100%); }

  .products { position: absolute; left: 230px; top: 2196px; width: 730px; height: 574px; }
  .products .divider { position: absolute; left: 368px; top: 0; width: 3px; height: 574px; background: var(--rule); }
  .product { position: absolute; top: 0; width: 300px; text-align: center; }
  .product.left { left: 0; }
  .product.right { left: 402px; }
  .pack { margin: 0 auto; border-radius: 12px; }
  .product.left .pack { width: 218px; height: 320px; margin-top: 55px; background: linear-gradient(180deg, #f08a1c, #f5a53c 50%, #e9771a); }
  .product.right .pack { width: 187px; height: 269px; margin-top: 81px; background: linear-gradient(180deg, #e8731e, #d96a1b 50%, #a34e1c); }
  .product h3 { font-size: 15px; font-weight: 400; line-height: 20px; }
  .product.left h3 { margin-top: 33px; }
  .product.right h3 { margin-top: 58px; }
  .price { margin-top: 18px; font-size: 28px; font-weight: 700; color: #444; }
  .product .button { margin-top: 14px; }

  .mascot { position: absolute; left: 825px; top: 2807px; width: 81px; height: 134px;
    background: linear-gradient(180deg, #e6b07a, #f4ece2 60%, #ffffff); border-radius: 40px 40px 0 0; }

  .footer {
    position: absolute; left: 0; top: 2941px; width: 1200px; height: 115px;
    background: var(--blue); color: var(--white); text-align: center; font-size: 13px; line-height: 24px; padding-top: 20px;
  }
  .footer a { color: var(--white); }
</style>
</head>
<body>
  <div class="preheader">
    <span class="view">Having trouble viewing this email? <a href="#">View it in your browser</a></span>
    <span class="forward"><a href="#">Forward to a Friend</a></span>
  </div>

  <header class="masthead">
    <span class="brand-name">Brisk Lane</span>
    <span class="brand-dot"></span>
  </header>

  <section class="article cockatiel">
    <div class="photo" role="img" aria-label="Photo of a grey cockatiel with a yellow crest"></div>
    <h2>Caring for your Cockatiel</h2>
    <p>Cockatiels are becoming increasingly popular as pets, they are less expensive than other larger breeds of parrot but aren't shy on personality! These beautiful birds are closely related to Cockatoos and are native to Australia. In the wild cockatiels are usually grey, this is mother natures way of camouflaging them, however these intelligent, social birds are well known for their bright orange cheeks and their yellow or grey crests...</p>
    <a class="button" href="#">read more</a>
  </section>
  <div class="rule" style="top:839px"></div>

  <section class="article frog">
    <div class="photo" role="img" aria-label="Photo of a green tree frog on a branch"></div>
    <h2>Caring for a Green Tree Frog</h2>
    <p>Originating from the Southeast United States the Green Treefrog (Hyla cinerea) is a popular amphibian to have at home. It is medium in size at 3.2-5.7 cm with long limbs, long digits, and sticky toe pads. The Green Tree frog is green with a white, yellow or sometimes iridescent stripe along each side of the body. The length of these stripes varies among some populations and may not be present at all. Additionally, yellow flecks are often found on the dorsum...</p>
    <a class="button" href="#">read more</a>
  </section>
  <div class="rule" style="top:1505px"></div>

  <section class="article horses">
    <div class="photo" role="img" aria-label="Photo of two horses on a hillside under a blue sky"></div>
    <h2>Understanding Horses</h2>
    <p>Horses are beautiful, trustworthy animals, building relationships with them can be rewarding as they tend to be lifelong. It is essential to understand the behavior of horses in order to build these relationships and to learn how to care for them correctly, of course each animal has their own personality, but there are certain things that all horses do...</p>
    <a class="button" href="#">read more</a>
  </section>
  <div class="rule" style="top:2143px"></div>

  <section class="products">
    <div class="product left">
      <div class="pack" role="img" aria-label="Product photo of an orange pouch of cat treats"></div>
      <h3>Snoozles Cat Treats (8 x 60g)</h3>
      <div class="price">£12.99</div>
      <a class="button" href="#">view details</a>
    </div>
    <div class="divider"></div>
    <div class="product right">
      <div class="pack" role="img" aria-label="Product photo of a pouch of cat treats"></div>
      <h3>Purrbites Cat Treats 65g</h3>
      <div class="price">£4.91</div>
      <a class="button" href="#">view details</a>
    </div>
  </section>

  <div class="mascot" role="img" aria-label="Illustration of a calico cat peeking over the footer"></div>

  <footer class="footer">
    This newsletter was sent to reader@inboxmail.example from Brisk Lane because you subscribed.<br>
    Rather not receive our newsletter anymore? <a href="#">Unsubscribe</a> instantly
  </footer>
</body>
</html>
```